Business Card Design

We need a design for business cards for our company. We have a logo. We teach EMT's and we are based out of Virginia. The information that will need to add would be, name, title, phone number, email, address. On the back of the business card would be "We help you, help others"

Target Market(s)

People that want to become EMT's

Colors

Designer to choose colors to be used in the design.

Requirements
Must have
• company logo

```html
<!DOCTYPE html>
<html lang="en">
<head>
<meta charset="utf-8">
<title>Rescue Ready Academy – Business Card</title>
<link rel="stylesheet" href="https://fonts.googleapis.com/css2?family=Lato:wght@400;700&family=Dancing+Script:wght@500&display=swap">
<style>
  :root {
    --canvas: #dcdddf;
    --card: #ffffff;
    --brand-red: #e8253f;
    --band-grey: #98a3aa;
    --text-grey: #8c8c8c;
    --band-text: #5f6a70;
  }
  * { margin: 0; padding: 0; box-sizing: border-box; }
  html, body {
    width: 1200px; height: 1200px; overflow: hidden;
    background: var(--canvas);
    font-family: "Lato", sans-serif;
  }
  .canvas { position: relative; width: 1200px; height: 1200px; }
  .card {
    position: absolute; left: 361px; width: 474px; height: 269px;
    background: var(--card); border-radius: 27px; overflow: hidden;
  }
  .card--front { top: 235px; }
  .card--back { top: 532px; }
  .brand {
    position: absolute; left: 85px; top: 78px; width: 300px; height: 40px;
    display: flex; align-items: center; gap: 10px;
  }
  .brand__mark {
    width: 34px; height: 34px; border-radius: 50%;
    background: var(--band-grey); flex: none;
  }
  .brand__name {
    color: var(--brand-red); font-weight: 700;
    font-size: 21px; line-height: 1; white-space: nowrap;
  }
  .holder { position: absolute; left: 140px; top: 184px; }
  .holder__name { color: var(--brand-red); font-size: 13px; }
  .holder__title { color: var(--text-grey); font-size: 10.5px; margin-top: 2px; }
  .band {
    position: absolute; left: 0; bottom: 0; width: 100%; height: 44px;
    background: var(--band-grey);
  }
  .band__accent {
    position: absolute; left: 0; top: 0; width: 130px; height: 100%;
    background: var(--brand-red);
  }
  .contact {
    position: absolute; left: 140px; top: 2px;
    list-style: none; color: var(--band-text); font-size: 8px; line-height: 13px;
  }
  .contact li { display: flex; align-items: center; gap: 4px; }
  .contact svg { width: 9px; height: 9px; fill: var(--band-text); }
  .tagline {
    position: absolute; left: 140px; top: 182px;
    font-family: "Dancing Script", cursive; font-weight: 500;
    font-size: 22px; color: var(--brand-red);
  }
</style>
</head>
<body>
<main class="canvas">
  <section class="card card--front" aria-label="Business card front">
    <div class="brand">
      <div class="brand__mark"></div>
      <p class="brand__name">Rescue Ready Academy</p>
    </div>
    <div class="holder">
      <p class="holder__name">Dana Whitfield, LCSW, LAADC</p>
      <p class="holder__title">Director &amp; Founder | Interventionist</p>
    </div>
    <div class="band">
      <div class="band__accent"></div>
      <ul class="contact">
        <li><svg viewBox="0 0 10 10"><path d="M2 0.5 L3.8 2.6 L2.9 3.7 Q4 6 6.3 7.1 L7.4 6.2 L9.5 8 L8.3 9.5 Q1 8 0.5 1.7 Z"/></svg>555-014-2290</li>
        <li><svg viewBox="0 0 10 10"><path d="M0.5 2 H9.5 V8 H0.5 Z"/></svg>hello@rescueready.com</li>
        <li><svg viewBox="0 0 10 10"><circle cx="5" cy="5" r="4.5"/></svg>Suite 12, 48 Elm Street, Richmond</li>
      </ul>
    </div>
  </section>

  <section class="card card--back" aria-label="Business card back">
    <div class="brand">
      <div class="brand__mark"></div>
      <p class="brand__name">Rescue Ready Academy</p>
    </div>
    <p class="tagline">We help you, help others</p>
    <div class="band">
      <div class="band__accent"></div>
    </div>
  </section>
</main>
</body>
</html>
```